Nature and Scenic Photographs Business Card Design

I require a simple business card using the illustration that I have provided

Industry/Entity Type

Business

Contact Information for Business Card

Gil Harlow
Mobile: 0436182057
Skype: gilbert.moray.harlow

```html
<!DOCTYPE html>
<html lang="en">
<head>
<meta charset="utf-8">
<title>Gil Harlow – Business Card</title>
<link rel="stylesheet" href="https://fonts.googleapis.com/css2?family=Comfortaa:wght@700&family=Arimo:wght@400&display=swap">
<style>
  :root {
    --page-bg: #e9ebee;
    --photo-top: #a9cdeb;
    --photo-bottom: #4a88b6;
    --stripe: #3d77c0;
    --stripe-light: #dbe8f6;
    --navy: #1b3864;
    --brand: #2b3070;
    --white: #ffffff;
  }
  html, body {
    margin: 0;
    padding: 0;
    width: 1200px;
    height: 1200px;
    overflow: hidden;
    background: var(--page-bg);
  }
  .business-card {
    position: absolute;
    left: 80px;
    top: 303px;
    width: 1040px;
    height: 594px;
    overflow: hidden;
    background: var(--navy);
    box-shadow: 0 6px 24px rgba(0,0,0,0.18);
  }
  .card-art {
    position: absolute;
    inset: 0;
    width: 100%;
    height: 100%;
    display: block;
  }
  .brand {
    position: absolute;
    right: 60px;
    top: 70px;
    display: flex;
    align-items: center;
    gap: 16px;
  }
  .brand-square {
    width: 34px;
    height: 34px;
    background: var(--brand);
  }
  .brand-name {
    margin: 0;
    font-family: "Comfortaa", sans-serif;
    font-weight: 700;
    font-size: 40px;
    line-height: 1;
    color: var(--brand);
  }
  .contact {
    position: absolute;
    left: 50px;
    top: 345px;
    color: var(--white);
  }
  .contact-name {
    margin: 0 0 22px 30px;
    font-family: "Comfortaa", sans-serif;
    font-weight: 700;
    font-size: 50px;
    line-height: 1.1;
  }
  .contact-line {
    margin: 0 0 16px;
    font-family: "Arimo", sans-serif;
    font-size: 28px;
    line-height: 1.2;
    letter-spacing: 0.5px;
  }
  .contact-line.mobile { margin-left: 14px; }
</style>
</head>
<body>
  <div class="business-card">
    <svg class="card-art" viewBox="0 0 1040 594" xmlns="http://www.w3.org/2000/svg">
      <defs>
        <linearGradient id="photo-tones" x1="0" y1="0" x2="0" y2="1">
          <stop offset="0" stop-color="var(--photo-top)"/>
          <stop offset="1" stop-color="var(--photo-bottom)"/>
        </linearGradient>
      </defs>
      <rect class="harbour-photo" role="img" aria-label="Photograph of a marina with moored yachts, a breakwater, beach and hills under a clear sky" x="0" y="0" width="1040" height="594" fill="url(#photo-tones)"/>
      <path class="wave-highlight" d="M0,262 C250,212 420,292 560,372 C700,452 880,480 1040,478 L1040,594 L0,594 Z" fill="var(--stripe-light)"/>
      <path class="wave-stripe" d="M0,270 C250,220 420,300 560,380 C700,460 880,488 1040,486 L1040,594 L0,594 Z" fill="var(--stripe)"/>
      <path class="wave-band" d="M0,300 C250,262 420,334 560,408 C700,482 880,508 1040,506 L1040,594 L0,594 Z" fill="var(--navy)"/>
    </svg>

    <div class="brand">
      <span class="brand-square"></span>
      <p class="brand-name">Tidewater Images</p>
    </div>

    <div class="contact">
      <p class="contact-name">Gil Harlow</p>
      <p class="contact-line mobile">Mobile: 0436182057</p>
      <p class="contact-line skype">Skype: gilbert.moray.harlow</p>
    </div>
  </div>
</body>
</html>
```